Consulting/ Manufacturers Representative Website

I need a website for a consulting/manufacturer representative company in Texas called Birchwell Venture Advisors. We Uncover and implement the right solution, at the right time, in the right way. We consult, we train, we offer project management, we offer performance improvement, we offer value creation, we turn stagnation into growth, and we offer corporate performance improvement.
I want the design to load on desktop and mobile, I want the site to look and feel professional like a large firm, and I want the site to be a marketing tool and establish a strong online presence.

Target Market(s)

City Governments, State Governments, County Governments, US Government, Power Plants, Refineries, Chemical Plants, Industrial customers

Industry/Entity Type

Consulting

Number of Pages Required

5+ page

Requirements
Must have
• mobile and desktop compatible, professional look, must be a fast website, company email and contact capabilities, contact page, company logo on website, SEO optimized, must display different industries served: Energy, Public (Government, Not For Profit, Educational), Transportation & Logistics, Business Services.
• Show that I help customers operate in a cleaner, safer and more economical way.
Nice to have
• news letter, news feed, show that company is principles based.
Should not have
• slow site, cheap look

```html
<!DOCTYPE html>
<html lang="en">
<head>
<meta charset="utf-8">
<title>Birchwell Venture Advisors — Consulting &amp; Manufacturer</title>
<link href="https://fonts.googleapis.com/css2?family=Montserrat:wght@400;500;600&family=Open+Sans:ital,wght@0,400;0,600;1,400&family=Roboto+Condensed:wght@700&display=swap" rel="stylesheet">
<style>
  :root{
    --navy:#0e3b7a;
    --navy-deep:#0a2d63;
    --blue:#1d5a9e;
    --blue-light:#2f76bd;
    --night:#0f1f3a;
    --ink:#2b2b2b;
    --muted:#6b6b6b;
    --grey-band:#e7e7e7;
    --line:#d6d6d6;
    --accent:#e8772e;
    --white:#ffffff;
  }
  *{box-sizing:border-box;margin:0;padding:0}
  html,body{width:1200px;height:4138px;overflow:hidden}
  body{position:relative;background:var(--white);font-family:"Open Sans",Arial,sans-serif;color:var(--ink)}
  h2.section-title{position:absolute;left:0;width:1200px;text-align:center;font-family:"Montserrat",Arial,sans-serif;font-weight:400;font-size:32px}

  /* header */
  .site-header{position:absolute;left:0;top:0;width:1200px;height:105px;background:var(--white)}
  .brand{position:absolute;left:116px;top:38px;display:flex;align-items:center;gap:8px}
  .brand-mark{width:14px;height:14px;background:var(--navy)}
  .brand-name{font-family:"Montserrat",Arial,sans-serif;font-weight:600;font-size:17px;color:var(--navy);letter-spacing:1px}
  .main-nav{position:absolute;top:44px;left:0;font-family:"Montserrat",Arial,sans-serif;font-size:16px;color:var(--ink)}
  .main-nav a{position:absolute;white-space:nowrap;color:inherit;text-decoration:none}
  .main-nav a.active{color:var(--navy)}
  .login{position:absolute;left:1021px;top:42px;width:62px;height:24px;border:1.5px solid var(--navy);color:var(--navy);font-size:14px;text-align:center;line-height:21px;font-family:"Montserrat",Arial,sans-serif}

  /* hero */
  .hero{position:absolute;left:0;top:105px;width:1200px;height:626px;
    clip-path:polygon(0 0,100% 0,100% 520px,1120px 535px,1040px 556px,960px 566px,880px 578px,800px 598px,720px 608px,650px 590px,600px 626px,550px 596px,470px 608px,390px 586px,300px 575px,200px 563px,120px 545px,0 522px)}
  .hero-photo{position:absolute;inset:0;background:linear-gradient(100deg,#5b6f86 0%,#8a9bb0 30%,#a7a39b 55%,#59636f 80%,#3b4657 100%)}
  .hero-shade{position:absolute;inset:0;background:linear-gradient(180deg,rgba(10,25,50,.15),rgba(10,25,50,.35))}
  .hero-title{position:absolute;left:0;top:285px;width:1200px;text-align:center;font-family:"Roboto Condensed",Arial,sans-serif;font-weight:700;font-size:44px;color:var(--white);letter-spacing:.5px}
  .hero-sub{position:absolute;left:0;top:333px;width:1200px;text-align:center;font-family:"Montserrat",Arial,sans-serif;font-size:36px;color:var(--white)}
  .hero-btn{position:absolute;left:519px;top:414px;width:160px;height:38px;border:2px solid var(--white);color:var(--white);font-family:"Montserrat",Arial,sans-serif;font-size:14px;font-weight:500;text-align:center;line-height:34px}
  .hero-arrow{position:absolute;top:253px;width:26px;height:26px;border-radius:50%;background:rgba(30,30,30,.55)}

  /* about */
  .about-frame{position:absolute;left:116px;top:844px;width:521px;height:323px;border:2px solid var(--navy)}
  .about-title{position:absolute;left:156px;top:885px;font-family:"Montserrat",Arial,sans-serif;font-size:32px;font-weight:400}
  .about-text{position:absolute;left:156px;top:944px;width:400px;font-size:14px;line-height:24px;color:#555;text-align:justify}
  .about-text p+p{margin-top:14px}
  .about-video{position:absolute;left:601px;top:894px;width:483px;height:312px;background:linear-gradient(135deg,#c5cbd3 0%,#7f8a97 45%,#3e4a5a 100%)}
  .play{position:absolute;left:806px;top:1007px;width:82px;height:82px;border-radius:50%;background:rgba(255,255,255,.85)}

  /* services */
  .services{position:absolute;left:0;top:1338px;width:1200px;height:566px;background:var(--grey-band)}
  .notch{position:absolute;left:580px;width:40px;height:20px;clip-path:polygon(0 0,100% 0,50% 100%)}
  .service-card{position:absolute;width:226px;height:243px;background:var(--white);text-align:center;padding-top:68px}
  .service-icon{position:absolute;top:-52px;left:71px;width:84px;height:84px}
  .service-card h3{font-family:"Montserrat",Arial,sans-serif;font-weight:500;font-size:16px;color:var(--ink)}
  .service-card p{margin:20px auto 0;width:170px;font-size:11.5px;line-height:16px;color:#7a7a7a}
  .read-more{display:inline-block;margin-top:20px;font-family:"Montserrat",Arial,sans-serif;font-size:13px;font-weight:500;color:var(--ink);padding-bottom:6px;border-bottom:2px solid var(--accent);border-image:linear-gradient(90deg,transparent 15%,var(--accent) 15%,var(--accent) 85%,transparent 85%) 1}

  /* what we do */
  .what{position:absolute;left:0;top:1904px;width:1200px;height:543px;background:linear-gradient(180deg,#2363a8 0%,#1b5698 60%,#16467f 100%);
    clip-path:polygon(0 0,100% 0,100% 455px,1130px 470px,1050px 478px,960px 470px,880px 490px,800px 498px,700px 488px,600px 503px,500px 494px,420px 492px,340px 476px,240px 474px,150px 462px,60px 478px,0 462px)}
  .what h2.section-title{color:var(--white);top:75px}
  .what-card{position:absolute;top:165px;width:464px;height:221px;display:flex}
  .what-photo{width:224px;height:100%;background:linear-gradient(135deg,#c9bda9,#8b8378 60%,#5c5a58)}
  .what-body{flex:1;background:var(--navy-deep);color:var(--white);padding:22px 22px 0 30px}
  .what-body h3{font-family:"Montserrat",Arial,sans-serif;font-weight:600;font-size:18px}
  .what-body p{margin-top:12px;font-size:12.5px;line-height:21px}
  .what-body .more{display:block;margin-top:10px;font-family:"Montserrat",Arial,sans-serif;font-size:12.5px;font-weight:600}

  /* news */
  .news-card{position:absolute;top:2643px;width:470px;height:419px;border:1px solid var(--line);background:var(--white)}
  .news-photo{width:100%;height:221px}
  .news-body{padding:20px 36px 0 36px}
  .news-date{font-family:"Montserrat",Arial,sans-serif;font-weight:600;font-size:14px;color:var(--ink)}
  .news-body h3{margin-top:14px;font-family:"Montserrat",Arial,sans-serif;font-weight:500;font-size:19px;color:var(--ink)}
  .news-body p{margin-top:12px;font-size:12px;line-height:18px;color:#8a8a8a}
  .news-more{display:inline-block;margin-top:18px;font-family:"Montserrat",Arial,sans-serif;font-size:12.5px;font-weight:500;padding-bottom:4px;border-bottom:1.5px solid var(--ink)}

  /* testimonial */
  .testimonial{position:absolute;left:0;top:3192px;width:1200px;height:519px;background:linear-gradient(180deg,#14284a 0%,#0f1f3a 55%,#0c1930 100%);
    clip-path:polygon(0 0,100% 0,100% 448px,1110px 466px,1020px 456px,930px 480px,840px 470px,760px 488px,650px 476px,560px 492px,470px 480px,380px 488px,300px 470px,200px 480px,120px 462px,0 470px)}
  .testimonial h2.section-title{color:var(--white);top:88px}
  .quote{position:absolute;left:171px;top:188px;width:866px;text-align:center;font-size:15px;line-height:26px;color:var(--white)}
  .quote-mark{position:absolute;font-family:Georgia,serif;font-size:46px;color:var(--white);line-height:1}
  .avatar{position:absolute;left:557px;top:287px;width:110px;height:110px;border-radius:50%;border:3px solid var(--white);background:linear-gradient(135deg,#b89a82,#5e4b40)}
  .t-arrow{position:absolute;top:326px}
  .t-name{position:absolute;left:0;top:410px;width:1200px;text-align:center;font-size:15px;font-style:italic;color:var(--white)}

  /* footer */
  .site-footer{position:absolute;left:0;top:3700px;width:1200px;height:438px;background:linear-gradient(90deg,#f3f2f0 0%,#ecece9 35%,#e4e6ea 70%,#eef0f3 100%);z-index:-1}
  .footer-brand{position:absolute;left:0;top:3855px;width:1200px;display:flex;justify-content:center;align-items:center;gap:8px}
  .footer-nav{position:absolute;top:3954px;left:0;font-family:"Montserrat",Arial,sans-serif;font-size:15px;color:var(--ink)}
  .footer-nav a{position:absolute;white-space:nowrap;color:inherit;text-decoration:none}
  .social{position:absolute;top:4001px;width:38px;height:38px;border-radius:50%;border:2px solid var(--ink)}
  .copyright{position:absolute;left:0;top:4064px;width:1200px;text-align:center;font-size:12.5px;color:var(--ink)}
</style>
</head>
<body>

<header class="site-header">
  <div class="brand"><span class="brand-mark"></span><span class="brand-name">BIRCHWELL</span></div>
  <nav class="main-nav">
    <a class="active" style="left:513px">Home</a>
    <a style="left:594px">About</a>
    <a style="left:674px">Services</a>
    <a style="left:775px">Projects</a>
    <a style="left:872px">Blog</a>
    <a style="left:942px">Contact</a>
  </nav>
  <div class="login">Login</div>
</header>

<section class="hero">
  <div class="hero-photo" role="img" aria-label="Consultant working at a laptop in a bright office"></div>
  <div class="hero-shade"></div>
  <div class="hero-arrow" style="left:103px"><svg width="26" height="26"><path d="M15 8l-5 5 5 5" fill="none" stroke="#fff" stroke-width="2"/></svg></div>
  <div class="hero-arrow" style="left:1080px"><svg width="26" height="26"><path d="M11 8l5 5-5 5" fill="none" stroke="#fff" stroke-width="2"/></svg></div>
  <div class="hero-title">BIRCHWELL VENTURE ADVISORS</div>
  <div class="hero-sub">Consulting &amp;Manufacturer</div>
  <div class="hero-btn">LEARN MORE</div>
</section>

<section class="about">
  <div class="about-frame"></div>
  <h2 class="about-title">About</h2>
  <div class="about-text">
    <p>It is a long established fact that a reader will be distracted by the readable content of a page when looking at its layout. The point of using Lorem Ipsum is that it has a more-or-less here, content here'.</p>
    <p>Many desktop publishing packages and web page editors now use Lorem Ipsum as their default model text, and a search for 'lorem ipsum' will uncover many web sites</p>
  </div>
  <div class="about-video" role="img" aria-label="Video still of an engineer at a desk with an industrial plant overlay"></div>
  <div class="play"><svg width="82" height="82"><path d="M33 25l24 16-24 16z" fill="#3b3b3b"/></svg></div>
</section>

<section class="services">
  <div class="notch" style="top:0;background:var(--white)"></div>
  <h2 class="section-title" style="top:76px">Our Services</h2>

  <div class="service-card" style="left:116px;top:210px">
    <svg class="service-icon" viewBox="0 0 84 84"><path d="M42 4L82 80H2z" fill="var(--navy)"/><circle cx="34" cy="52" r="5" fill="#fff"/><circle cx="50" cy="52" r="5" fill="#fff"/><path d="M25 68a9 9 0 0118 0zM41 68a9 9 0 0118 0z" fill="#fff"/></svg>
    <h3>We consult</h3>
    <p>It is a long established fact that a reader will be tracted by the readable content of a page when looking</p>
    <span class="read-more">READ MORE</span>
  </div>
  <div class="service-card" style="left:361px;top:213px">
    <svg class="service-icon" viewBox="0 0 84 84"><path d="M42 4L82 80H2z" fill="var(--navy)"/><rect x="29" y="48" width="26" height="17" rx="1" fill="none" stroke="#fff" stroke-width="3"/><path d="M37 70h10" stroke="#fff" stroke-width="3"/></svg>
    <h3>We train</h3>
    <p>It is a long established fact that a reader will be tracted by the readable content of a page when looking</p>
    <span class="read-more">READ MORE</span>
  </div>
  <div class="service-card" style="left:607px;top:210px">
    <svg class="service-icon" viewBox="0 0 84 84"><path d="M42 4L82 80H2z" fill="var(--navy)"/><circle cx="42" cy="58" r="10" fill="none" stroke="#fff" stroke-width="5" stroke-dasharray="4 3"/><circle cx="42" cy="58" r="5" fill="#fff"/></svg>
    <h3>Project management</h3>
    <p>It is a long established fact that a reader will be tracted by the readable content of a page when looking</p>
    <span class="read-more">READ MORE</span>
  </div>
  <div class="service-card" style="left:853px;top:216px">
    <svg class="service-icon" viewBox="0 0 84 84"><path d="M42 4L82 80H2z" fill="var(--navy)"/><path d="M34 45h12l6 6v19H34z" fill="#fff"/><path d="M38 56h10M38 61h10M38 66h10" stroke="var(--navy)" stroke-width="1.6"/></svg>
    <h3>Value creation</h3>
    <p>It is a long established fact that a reader will be tracted by the readable content of a page when looking</p>
    <span class="read-more">READ MORE</span>
  </div>
</section>

<section class="what">
  <h2 class="section-title">What We do</h2>
  <div class="what-card" style="left:121px">
    <div class="what-photo" role="img" aria-label="Two colleagues reviewing work on a laptop"></div>
    <div class="what-body">
      <h3>Porro quisquam</h3>
      <p>It is a long established fact that a reader will be distracted by the readable content of a page when looking at its layout. The point of using Lorem</p>
      <span class="more">READ MORE</span>
    </div>
  </div>
  <div class="what-card" style="left:618px">
    <div class="what-photo" role="img" aria-label="Business meeting across a desk" style="background:linear-gradient(135deg,#d6dbe0,#8c96a2 55%,#4c5764)"></div>
    <div class="what-body">
      <h3>Porro quisquam</h3>
      <p>It is a long established fact that a reader will be distracted by the readable content of a page when looking at its layout. The point of using Lorem</p>
      <span class="more">READ MORE</span>
    </div>
  </div>
</section>

<section class="news">
  <h2 class="section-title" style="top:2558px">Our News</h2>
  <article class="news-card" style="left:130px">
    <div class="news-photo" role="img" aria-label="Hands signing documents beside a laptop" style="background:linear-gradient(135deg,#3f5f86,#9fb3c8 50%,#e6e9ed)"></div>
    <div class="news-body">
      <div class="news-date">MARCH 20, 2018</div>
      <h3>Neque porro quisquam est qui</h3>
      <p>Praesent elementum elit at tellus nec ultricies sit amet porttitor mattis enim In massa libero interdum nec interdum vel blandit</p>
      <span class="news-more">READ MORE</span>
    </div>
  </article>
  <article class="news-card" style="left:618px">
    <div class="news-photo" role="img" aria-label="Wind turbines and solar panels in front of a city skyline" style="background:linear-gradient(180deg,#3f7fd0 0%,#8fc0ee 55%,#3b5f2e 80%,#2a3e52 100%)"></div>
    <div class="news-body">
      <div class="news-date">MARCH 20, 2018</div>
      <h3>Dolorem ipsum quia dolor sit amet</h3>
      <p>Praesent elementum elit at tellus nec ultricies sit amet porttitor mattis enim In massa libero interdum nec interdum</p>
      <span class="news-more">READ MORE</span>
    </div>
  </article>
</section>

<section class="testimonial">
  <div class="notch" style="top:0;background:var(--white)"></div>
  <h2 class="section-title">Testimonial</h2>
  <span class="quote-mark" style="left:136px;top:178px">&ldquo;</span>
  <p class="quote">It has survived not only five centuries, but also the leap into electronic typesetting, remaining essentially unchanged. It was popularised in the 1960s with the release of Typeleaf sheets containing Lorem Ipsum passages, and more recently with desktop publishing software like Pagewright Studio including versions of Lorem Ipsum</p>
  <span class="quote-mark" style="left:936px;top:232px">&rdquo;</span>
  <div class="avatar" role="img" aria-label="Portrait of the client giving the testimonial"></div>
  <svg class="t-arrow" style="left:514px" width="20" height="30"><path d="M16 3L4 15l12 12" fill="none" stroke="#fff" stroke-width="2.5"/></svg>
  <svg class="t-arrow" style="left:688px" width="20" height="30"><path d="M4 3l12 12L4 27" fill="none" stroke="#fff" stroke-width="2.5"/></svg>
  <div class="t-name">Neque porro quisquam</div>
</section>

<footer>
  <div class="site-footer" role="img" aria-label="Faint city skyline and businessman in the background"></div>
  <div class="footer-brand"><span class="brand-mark"></span><span class="brand-name">BIRCHWELL</span></div>
  <nav class="footer-nav">
    <a style="left:396px">Home</a>
    <a style="left:472px">About</a>
    <a style="left:548px">Service</a>
    <a style="left:637px">Project</a>
    <a style="left:721px">Contact us</a>
  </nav>
  <span class="social" style="left:480px" aria-label="Professional network"></span>
  <span class="social" style="left:530px" aria-label="Microblog"></span>
  <span class="social" style="left:580px" aria-label="Social page"></span>
  <span class="social" style="left:629px" aria-label="Pin board"></span>
  <span class="social" style="left:679px" aria-label="Photo sharing"></span>
  <div class="copyright">Copyright © 2018 All Rights Reserved</div>
</footer>

</body>
</html>
```